Communication and Marketing agency needs a new presentation card

We are a group of communication and marketing agencies specialized in companies that are in the logistics and industrial sector. The head agency is VELUNEX Grupo and the group consists of 4 agencies: VELUNEX Media, VELUNEX Digital, VELUNEX Research and PlanoDeImagenes. We hace 4 offices in Spain (Madrid, Barcelona, Valencia and Murcia). We are looking for a clean and attractive design that transmits our experience, brand presence in the market and knowledge to those who receive the card.It has to maintain the colors of the logo that is attached.
logistics and industrial sector
Marketing department
Clean and attractive design

```html
<!DOCTYPE html>
<html lang="en">
<head>
<meta charset="utf-8">
<title>VELUNEX Grupo – Business Card</title>
<link href="https://fonts.googleapis.com/css2?family=Open+Sans:wght@400;600&family=Oswald:wght@600&display=swap" rel="stylesheet">
<style>
  :root {
    --brand-red: #b41f2a;
    --paper: #f2f2f2;
    --ink-grey: #4a4848;
    --backdrop: #1f1f1f;
    --white: #ffffff;
  }
  * { margin: 0; padding: 0; box-sizing: border-box; }
  html, body { width: 1200px; height: 900px; overflow: hidden; }
  body {
    background: var(--backdrop);
    font-family: "Open Sans", Arial, sans-serif;
    display: flex;
    flex-direction: column;
    align-items: center;
    justify-content: center;
    gap: 40px;
  }
  .card {
    width: 640px;
    height: 366px;
    position: relative;
    overflow: hidden;
  }
  .wordmark {
    font-family: "Open Sans", Arial, sans-serif;
    font-weight: 600;
    letter-spacing: 2px;
    white-space: nowrap;
  }

  /* Reverse side */
  .card-back {
    background: var(--brand-red);
    display: flex;
    align-items: center;
    justify-content: center;
  }
  .card-back .wordmark { color: var(--white); font-size: 46px; }

  /* Front side */
  .card-front { background: var(--paper); }
  .card-front .wordmark {
    position: absolute;
    top: 58px;
    left: 0; right: 0;
    text-align: center;
    color: var(--brand-red);
    font-size: 46px;
  }
  .person {
    position: absolute;
    top: 158px;
    left: 0; right: 0;
    text-align: center;
  }
  .person-name {
    font-family: "Oswald", "Arial Narrow", sans-serif;
    font-weight: 600;
    font-size: 24px;
    color: var(--brand-red);
    letter-spacing: 1px;
    line-height: 1.1;
  }
  .person-role {
    font-size: 14px;
    color: var(--ink-grey);
  }
  .divider {
    position: absolute;
    left: 0; right: 0;
    top: 222px;
    height: 4px;
    background: var(--ink-grey);
  }
  .contact-band {
    position: absolute;
    left: 0; right: 0;
    top: 232px;
    bottom: 0;
    background: var(--brand-red);
    color: var(--white);
    display: flex;
    justify-content: space-between;
    align-items: flex-end;
    padding: 0 36px 34px;
    font-size: 13px;
    line-height: 1.55;
  }
  .contact-list { list-style: none; }
  .contact-list li { display: flex; align-items: center; gap: 8px; }
  .contact-list svg { width: 11px; height: 11px; fill: var(--white); flex: none; }
  .address { text-align: right; align-self: center; margin-top: -10px; }
</style>
</head>
<body>

  <section class="card card-back" aria-label="Card reverse">
    <span class="wordmark">VELUNEX Grupo</span>
  </section>

  <section class="card card-front" aria-label="Card front">
    <span class="wordmark">VELUNEX Grupo</span>

    <div class="person">
      <div class="person-name">LUCAS FERRANDO</div>
      <div class="person-role">Founder</div>
    </div>

    <div class="divider"></div>

    <div class="contact-band">
      <ul class="contact-list">
        <li>
          <svg viewBox="0 0 24 24" aria-hidden="true"><path d="M6.6 10.8a15.1 15.1 0 0 0 6.6 6.6l2.2-2.2a1 1 0 0 1 1-.25 11.4 11.4 0 0 0 3.6.57 1 1 0 0 1 1 1V20a1 1 0 0 1-1 1A17 17 0 0 1 3 4a1 1 0 0 1 1-1h3.5a1 1 0 0 1 1 1c0 1.25.2 2.45.57 3.57a1 1 0 0 1-.25 1z"/></svg>
          (000) 555-210-00
        </li>
        <li>
          <svg viewBox="0 0 24 24" aria-hidden="true"><path d="M2 5h20v14H2z M2 5l10 8 10-8" stroke="#b41f2a" stroke-width="1.5"/></svg>
          info@velunexgrupo.com
        </li>
        <li>
          <svg viewBox="0 0 24 24" aria-hidden="true"><circle cx="12" cy="12" r="10"/><path d="M2 12h20M12 2c3 3 3 17 0 20M12 2c-3 3-3 17 0 20" stroke="#b41f2a" stroke-width="1.5" fill="none"/></svg>
          www.velunexgrupo.com
        </li>
      </ul>
      <address class="address" style="font-style:normal">
        120-140 Calle Norte<br>
        MD 28004, Spain
      </address>
    </div>
  </section>

</body>
</html>
```